Design CD-Velvet Tadpole/WAIT FOR THE ORANGE TRAIN
Zielgruppe
Wir sind Velvet Tadpole eine INDIE/ALTERNATIVE Band.. bestehend aus 4 Jungs im alter von durchschnittlich 22 Jahren. Wir suchen ein Design für unsere 2. Platte die den Namen 'WAIT FOR THE ORANGE TRAIN' trägt. Im gleichnamigen Song geht es um einen Menschen der am Limit lebt und jeden Moment ohne Rücksicht auf andere auskostet.. als er eines Tages versteht wie er den Menschen die er liebt damit Schaden zufügt, verspricht er seiner LIEBE:'I SWEAR I WILL WAIT FOR THE ORANGE TRAIN'..'im nächsten Leben werde ich ein besserer Typ sein.
Unsere Musik zeichnet sich durch 3 Stimmigen Gesang, verspielte teilweise psychodelische Sounds und eingängige Melodien die sich zu unserem Markenzeichen entwickelt haben aus.
Aufgabenstellung
Das Design soll Modern,verspielt,Bunt, gerne etwas abstrakt und vor allem Grafisch (nicht im realistic style) sein.
Beispielbilder in welche Richtung es gehen soll lege ich in den Anhang.

```html
<!DOCTYPE html>
<html lang="en">
<head>
<meta charset="utf-8">
<title>Velvet Tadpole – Wait for the Orange Train</title>
<link rel="stylesheet" href="https://fonts.googleapis.com/css2?family=Orbitron:wght@400;500&display=swap">
<style>
  :root {
    --stage: #5d5c66;
    --ink: #141214;
    --title-light: #f1eeee;
    --gold: #e6c23a;
    --lemon: #e8dc5a;
    --cream: #f1dcb8;
    --peach: #eea070;
    --rose: #ee8aa0;
    --crimson: #e61f4d;
    --amber: #d99a56;
  }
  * { margin: 0; padding: 0; box-sizing: border-box; }
  html, body {
    width: 1200px;
    height: 848px;
    overflow: hidden;
    background: var(--stage);
  }
  .canvas {
    position: relative;
    width: 1200px;
    height: 848px;
  }
  .cover {
    position: absolute;
    left: 220px;
    top: 44px;
    width: 760px;
    height: 760px;
    overflow: hidden;
  }
  .cover-artwork {
    position: absolute;
    inset: 0;
    background:
      linear-gradient(180deg, rgba(241,220,184,0.9) 0%, rgba(241,220,184,0) 24%),
      linear-gradient(0deg, rgba(217,154,86,0.85) 0%, rgba(217,154,86,0) 24%),
      linear-gradient(90deg,
        var(--gold) 0%,
        var(--lemon) 30%,
        var(--peach) 52%,
        var(--rose) 78%,
        var(--crimson) 88%,
        var(--crimson) 100%);
  }
  .band-name {
    position: absolute;
    top: 62px;
    left: 0;
    width: 100%;
    text-align: center;
    font-family: "Orbitron", sans-serif;
    font-weight: 500;
    font-size: 46px;
    letter-spacing: 0.42em;
    padding-left: 0.42em;
    color: var(--ink);
  }
  .album-title {
    position: absolute;
    top: 598px;
    left: 0;
    width: 100%;
    text-align: center;
    font-family: "Orbitron", sans-serif;
    font-weight: 400;
    font-size: 28px;
    line-height: 60px;
    letter-spacing: 0.5em;
    padding-left: 0.5em;
    color: var(--title-light);
  }
</style>
</head>
<body>
  <main class="canvas">
    <section class="cover">
      <div class="cover-artwork" role="img" aria-label="Motion-blurred photograph of a figure standing in a warm yellow-to-crimson lit room"></div>
      <h1 class="band-name">Velvet Tadpole</h1>
      <h2 class="album-title">WAIT FOR THE<br>ORANGE TRAIN</h2>
    </section>
  </main>
</body>
</html>
```